"BREAKING NEWS!" Fitness photos needed

Hello.... We are creating our new ads for Pellumra and Quorvidel and we need some photos manipulated and text added.

We have 5 photos total that we would like to have the Headline read "Breaking News" and we'll be split testing two different quotes, so I'd like to have:

AD #1:
Breaking News - Finally! Ridgecrest Gets the Gym That Actually Delivers Results (and It's Fun!)

And then a second set on the same photos that read:

AD #2:
Breaking News - Ridgecrest Residents Ditch Boring Workouts for This Life-Changing Fitness Experience

I'd like the photos to pop and stand out, so if color corrections need to be done, please feel free.

I've attached all photos and an example photo that DOES NOT need to be the same. It's just an example I saw that caught my eye, but I feel could be done better.

Thank you!

```html
<!DOCTYPE html>
<html lang="en">
<head>
<meta charset="utf-8">
<title>Breaking News – Fitness Ads</title>
<link rel="stylesheet" href="https://fonts.googleapis.com/css2?family=Bebas+Neue&family=Josefin+Sans:wght@300&family=Montserrat:wght@400;700&display=swap">
<style>
  :root {
    --sheet: #f4f4f4;
    --yellow: #ecc100;
    --olive: #8a7200;
    --black: #000000;
    --maroon-dark: #4a1f2a;
    --maroon: #9c2335;
    --white: #ffffff;
    --photo-a: #5b5a5e;
    --photo-b: #b9b4ae;
    --photo-c: #d7b23a;
  }
  html, body {
    margin: 0;
    padding: 0;
    width: 808px;
    height: 1200px;
    overflow: hidden;
    background: var(--sheet);
  }
  .ad {
    position: absolute;
    left: 132px;
    width: 544px;
    height: 544px;
    display: block;
  }
  .ad--finally { top: 45px; }
  .ad--ditch { top: 620px; }
  .headline-bebas { font-family: "Bebas Neue", sans-serif; fill: var(--black); }
  .deck-bold { font-family: "Montserrat", sans-serif; font-weight: 700; fill: var(--black); }
  .headline-thin { font-family: "Josefin Sans", sans-serif; font-weight: 300; fill: var(--white); }
  .deck-light { font-family: "Montserrat", sans-serif; font-weight: 400; fill: var(--white); }
</style>
</head>
<body>

<!-- Ad 1: yellow / black angular layout -->
<svg class="ad ad--finally" viewBox="0 0 646 646" xmlns="http://www.w3.org/2000/svg">
  <defs>
    <linearGradient id="photoTone" x1="0" y1="0" x2="1" y2="1">
      <stop offset="0" stop-color="var(--photo-b)"/>
      <stop offset="1" stop-color="var(--photo-a)"/>
    </linearGradient>
    <linearGradient id="photoToneGym" x1="1" y1="0" x2="0" y2="1">
      <stop offset="0" stop-color="var(--photo-c)"/>
      <stop offset="0.35" stop-color="var(--photo-b)"/>
      <stop offset="1" stop-color="var(--photo-a)"/>
    </linearGradient>
  </defs>
  <rect class="panel-yellow" width="646" height="646" fill="var(--yellow)"/>
  <polygon class="band-olive" points="0,246 0,436 111,436" fill="var(--olive)"/>
  <polygon class="band-black-top" points="233,0 343,0 293,106 352,280" fill="var(--black)"/>
  <polygon class="band-black-right" points="403,286 646,286 646,646 603,646" fill="var(--black)"/>
  <polygon class="band-black-lower" points="197,380 385,380 533,646 358,646" fill="var(--black)"/>
  <polygon class="photo-kick" role="img" aria-label="Photo: instructor doing a high kick leading a group fitness class in the gym"
           points="343,0 646,0 646,226 613,286 353,286 293,106" fill="url(#photoToneGym)"/>
  <polygon class="photo-squat" role="img" aria-label="Photo: members doing dumbbell goblet squats beside step platforms"
           points="153,376 223,254 388,254 433,376 388,498 243,498" fill="url(#photoTone)"/>
  <text class="headline-bebas" x="33" y="153" font-size="74" textLength="242" lengthAdjust="spacingAndGlyphs">BREAKING</text>
  <text class="headline-bebas" x="33" y="208" font-size="50" textLength="243" lengthAdjust="spacingAndGlyphs">NEWS - FINALLY!</text>
  <text class="deck-bold" font-size="20.5">
    <tspan x="33" y="521">Ridgecrest Gets</tspan>
    <tspan x="33" y="546">the Gym That</tspan>
    <tspan x="33" y="571">Actually Delivers</tspan>
    <tspan x="33" y="596">Results (and It's Fun!)</tspan>
  </text>
</svg>

<!-- Ad 2: maroon layout with curved photo and circle inset -->
<svg class="ad ad--ditch" viewBox="0 0 646 646" xmlns="http://www.w3.org/2000/svg">
  <defs>
    <linearGradient id="maroonWash" x1="1" y1="0" x2="0" y2="1">
      <stop offset="0" stop-color="var(--maroon-dark)"/>
      <stop offset="1" stop-color="var(--maroon)"/>
    </linearGradient>
    <linearGradient id="photoToneWide" x1="0" y1="0" x2="1" y2="1">
      <stop offset="0" stop-color="var(--photo-c)"/>
      <stop offset="0.3" stop-color="var(--photo-b)"/>
      <stop offset="1" stop-color="var(--photo-a)"/>
    </linearGradient>
    <linearGradient id="photoToneRound" x1="1" y1="0" x2="0" y2="1">
      <stop offset="0" stop-color="var(--photo-c)"/>
      <stop offset="0.4" stop-color="var(--photo-b)"/>
      <stop offset="1" stop-color="var(--photo-a)"/>
    </linearGradient>
  </defs>
  <rect class="panel-maroon" width="646" height="646" fill="url(#maroonWash)"/>
  <path class="photo-squat-wide" role="img" aria-label="Photo: group doing dumbbell goblet squats at step platforms"
        d="M0 0 H473 C480 180 360 330 0 366 Z" fill="url(#photoToneWide)"
        stroke="var(--white)" stroke-width="6"/>
  <circle class="photo-kick-round" role="img" aria-label="Photo: instructor doing a high kick in a group class"
          cx="475" cy="292" r="140" fill="url(#photoToneRound)" stroke="var(--white)" stroke-width="5"/>
  <text class="headline-thin" x="45" y="459" font-size="75" textLength="228" lengthAdjust="spacingAndGlyphs">Breaking</text>
  <text class="headline-thin" x="45" y="534" font-size="90" textLength="191" lengthAdjust="spacingAndGlyphs">NEWS</text>
  <text class="deck-light" font-size="20.5">
    <tspan x="45" y="580" textLength="461" lengthAdjust="spacingAndGlyphs">Ridgecrest Residents Ditch Boring Workouts</tspan>
    <tspan x="45" y="605" textLength="430" lengthAdjust="spacingAndGlyphs">for This Life-Changing Fitness Experience</tspan>
  </text>
</svg>

</body>
</html>
```